THE MARKETPLACE FOR WAREHOUSE, the new way of doing logistics

We need an avant-garde, modern, minimalist and elegant web design for our company called VELMIRA. This company represents the future of logistics, where users can find multiple offers of spaces (warehouse) in one place and other users can offer their available spaces to generate an extra cash inflow. A sample of this company is www.quobly.com, a US company that has developed this business. The closest thing to this type of business is NESTORIA, since it develops a similar model for people who offer spaces in their homes and people who need a space for a limited time. My domain site is www.velmira.com, where is the logo of my company. spanish- ------------------------------------------------ ---------------------------------------------- We need a web design avant-garde, modern, minimalist and elegant for our company called VELMIRA. This company represents the future of logistics, where users can find multiple offers of spaces (wineries) in one place and other users can offer their available spaces to generate an extra profit. A sample of this company is www.quobly.com, a US company that has developed this business. The closest thing to this type of business is NESTORIA, since it develops a similar model for people who offer spaces in their homes and people who need a space for a limited time. My domain site is www.velmira.com, where is the logo of my company.

Target Market(s)

Companies, entrepreneurs, Companies, entrepreneurs,

Industry/Entity Type

Logistic

Number of Pages Required

5+ page

Colors
0d5aa6
ffffff
000000

Requirements
Must have
• A sober and minimalist homepage type plindo, NeStr. That is intuitive, must have spaces for advertising banners. You must always highlight the company logo. A sober and minimalist homepage like plindo, NeStr. That is intuitive, must have spaces for advertising banners. Must always highlight the company logo.

```html
<!DOCTYPE html>
<html lang="en">
<head>
<meta charset="utf-8">
<title>VELMIRA – The marketplace for warehouses</title>
<link href="https://fonts.googleapis.com/css2?family=Raleway:wght@500;600;700;800&family=Open+Sans:ital,wght@0,400;0,600;0,700;1,400&display=swap" rel="stylesheet">
<style>
:root{
  --brand:#0d5aa6;
  --brand-dark:#0d3f8f;
  --ink:#111;
  --text:#555;
  --muted:#888;
  --white:#fff;
  --pale:#f2f6fb;
  --line:#c9d3de;
  --star:#f2c200;
  --ad-green:#a6c93a;
  --ad-red:#e3212a;
}
*{margin:0;padding:0;box-sizing:border-box}
html,body{width:1200px;height:3905px;overflow:hidden;background:var(--white)}
body{position:relative;font-family:"Open Sans",sans-serif;color:var(--text)}
.abs{position:absolute}
h1,h2,h3,h4{font-family:"Raleway",sans-serif;color:var(--ink)}

/* header */
.header{position:absolute;left:0;top:0;width:1200px;height:96px;background:var(--white)}
.logo{position:absolute;display:flex;align-items:center;gap:10px}
.logo .mark{width:44px;height:44px;border-radius:50%;border:4px solid var(--brand)}
.logo .name{font-family:"Raleway",sans-serif;font-weight:800;color:var(--brand);letter-spacing:2px}
.nav{position:absolute;left:432px;top:40px;display:flex;gap:38px;font-family:"Raleway",sans-serif;font-weight:700;font-size:16px;color:var(--ink)}
.nav .active{color:var(--brand)}
.search{position:absolute;left:945px;top:42px}
.login{position:absolute;left:994px;top:31px;width:105px;height:44px;border:2px solid var(--brand);border-radius:22px;color:var(--brand);font-family:"Raleway",sans-serif;font-weight:800;font-size:16px;display:flex;align-items:center;justify-content:center;gap:6px}

/* hero */
.hero{position:absolute;left:0;top:96px;width:1200px;height:555px;background:linear-gradient(180deg,#6e6a62 0%,#8a8477 40%,#5d5a54 100%)}
.hero .shade{position:absolute;inset:0;background:rgba(20,30,45,.35)}
.hero-title{position:absolute;left:0;width:1200px;top:70px;text-align:center;font-family:"Raleway",sans-serif;font-weight:700;font-size:112px;letter-spacing:22px;color:var(--white)}
.hero-sub{position:absolute;left:0;width:1200px;top:196px;text-align:center;font-family:"Open Sans",sans-serif;font-size:26px;color:var(--white)}
.hero-btn{position:absolute;top:258px;width:169px;height:49px;border:2px solid var(--white);border-radius:25px;color:var(--white);font-family:"Raleway",sans-serif;font-weight:700;font-size:16px;display:flex;align-items:center;justify-content:center}
.dots{position:absolute;top:489px;left:572px;display:flex;gap:6px}
.dots span{width:11px;height:11px;border-radius:50%;border:2px solid var(--white)}
.dots span.on{background:var(--white)}

/* ad banner */
.ad{position:absolute;left:187px;top:690px;width:823px;height:101px;background:var(--ad-green);overflow:hidden}
.ad .tag{position:absolute;left:0;top:0;width:150px;height:101px;background:var(--ad-red);clip-path:polygon(0 0,80% 0,100% 50%,80% 100%,0 100%);color:var(--white);font-family:"Open Sans",sans-serif;font-weight:700;font-size:21px;line-height:24px;padding:24px 0 0 22px}
.ad .product{position:absolute;left:180px;top:14px;width:300px;height:74px;background:linear-gradient(90deg,#8a8d92,#c9cbce 45%,#4d6b8a)}
.ad .head{position:absolute;left:500px;top:18px;font-size:20px;color:var(--white);font-weight:600}
.ad .small{position:absolute;left:500px;top:45px;font-size:11px;color:#2d3a10}
.ad .more{position:absolute;left:500px;top:64px;width:84px;height:20px;background:var(--ad-red);color:var(--white);font-size:10px;font-weight:700;display:flex;align-items:center;justify-content:center}

/* welcome */
.welcome-box{position:absolute;left:99px;top:869px;width:596px;height:425px;border:1px solid #8a8a8a}
.welcome-box h2{position:absolute;left:55px;top:50px;font-size:35px;font-weight:800}
.welcome-box p{position:absolute;left:55px;top:116px;width:420px;font-size:14.5px;line-height:27px;color:var(--text)}
.btn-outline{position:absolute;border:2px solid var(--brand-dark);border-radius:26px;color:var(--ink);font-family:"Raleway",sans-serif;font-weight:800;display:flex;align-items:center;justify-content:center}
.video{position:absolute;left:633px;top:914px;width:468px;height:338px;background:linear-gradient(135deg,#9b7b55,#c9a277 45%,#5a6470);box-shadow:0 4px 14px rgba(0,0,0,.25)}
.video .play{position:absolute;left:206px;top:141px;width:60px;height:60px;border-radius:50%;background:var(--white);box-shadow:0 0 0 6px rgba(255,255,255,.35)}

/* solutions */
.solutions{position:absolute;left:0;top:1385px;width:1200px;height:554px;background:var(--pale)}
.section-title{position:absolute;left:0;width:1200px;text-align:center;font-size:35px;font-weight:800}
.sol{position:absolute;top:170px;width:300px}
.sol svg{display:block}
.sol h3{position:absolute;top:128px;font-size:25px;font-weight:600;white-space:nowrap}
.sol p{position:absolute;top:173px;width:300px;font-size:14.5px;line-height:26px}
.read{position:absolute;font-family:"Raleway",sans-serif;font-weight:800;font-size:14.5px;color:var(--brand-dark)}

/* reviews */
.reviews{position:absolute;left:0;top:1939px;width:1200px;height:404px;background:var(--brand-dark)}
.reviews .section-title{color:var(--white)}
.arrow-btn{position:absolute;top:214px;width:38px;height:38px;border-radius:50%;border:2px solid rgba(255,255,255,.75);display:flex;align-items:center;justify-content:center}
.review{position:absolute;top:156px;width:330px}
.avatar{position:absolute;left:0;top:0;width:74px;height:74px;border-radius:50%;border:3px solid var(--white);background:linear-gradient(160deg,#c9b8a8,#8f7a68)}
.quote{position:absolute;left:90px;top:4px;width:240px;color:var(--white);font-style:italic;font-size:12.5px;line-height:24px}
.quote b{font-family:"Raleway",sans-serif;font-size:26px;font-style:normal;font-weight:800;vertical-align:-8px;margin-right:6px}
.who{position:absolute;left:90px;top:97px;color:var(--white);font-size:10px;line-height:17px}
.who strong{font-weight:700;letter-spacing:.5px}
.who em{display:block}
.stars{position:absolute;left:90px;top:156px;display:flex;gap:4px}

/* blog */
.blog-title{top:2425px}
.post{position:absolute;top:2509px;width:323px}
.post .img{width:323px;height:211px}
.post h3{margin-top:38px;font-size:21px;font-weight:700}
.meta{margin-top:10px;display:flex;align-items:center;gap:8px;font-size:12.5px;color:var(--muted)}
.meta .sep{width:1px;height:14px;background:var(--muted);margin:0 6px}
.post p{margin-top:10px;font-size:13px;line-height:23px}
.post .read{position:static;display:block;margin-top:8px}

/* contact */
.contact-img{position:absolute;left:0;top:3004px;width:586px;height:476px;background:linear-gradient(180deg,#c7cdd3 0%,#9aa4ad 35%,#b48a58 60%,#d5d8dc 100%)}
.contact{position:absolute;left:586px;top:3004px;width:614px;height:476px;background:var(--pale)}
.contact h2{position:absolute;left:52px;top:68px;font-size:35px;font-weight:800}
.field{position:absolute;height:42px;border:1px solid #9aa3ad;background:var(--white);font-size:14px;color:#555;padding:10px 14px}
.submit{position:absolute;left:52px;top:364px;width:130px;height:45px;border-radius:23px;background:var(--brand-dark);color:var(--white);font-family:"Raleway",sans-serif;font-weight:800;font-size:16px;display:flex;align-items:center;justify-content:center}

/* footer */
.footer h4{position:absolute;top:3575px;font-size:18px;font-weight:700}
.links{position:absolute;left:409px;top:3618px;font-size:12.5px;line-height:25px;color:#444;list-style:none}
.news-text{position:absolute;left:601px;top:3624px;width:250px;font-size:13px;line-height:22px;color:#444}
.news-input{position:absolute;left:601px;top:3678px;width:255px;height:34px;border-bottom:1px solid var(--line);font-size:12.5px;color:var(--muted);padding-top:8px}
.subscribe{position:absolute;left:601px;top:3726px;width:100px;height:34px;font-size:12px}
.contact-item{position:absolute;left:919px;display:flex;gap:14px;font-size:12.5px;line-height:21px;color:#444}
.divider{position:absolute;left:99px;top:3808px;width:1002px;height:1px;background:#d8dde3}
.copy{position:absolute;left:99px;top:3846px;font-size:12.5px;color:#444}
.social{position:absolute;top:3836px;width:38px;height:38px;border-radius:50%;border:2px solid var(--brand-dark)}
</style>
</head>
<body>

<header class="header">
  <div class="logo" style="left:99px;top:23px">
    <span class="mark"></span><span class="name" style="font-size:36px">VELMIRA</span>
  </div>
  <nav class="nav">
    <span class="active">HOME</span><span>ABOUT</span><span>SOLUTIONS</span><span>BLOG</span><span>CONTACT US</span>
  </nav>
  <svg class="search" width="20" height="20" viewBox="0 0 20 20"><circle cx="8" cy="8" r="6" fill="none" stroke="#111" stroke-width="2.5"/><line x1="12.5" y1="12.5" x2="18" y2="18" stroke="#111" stroke-width="2.8"/></svg>
  <div class="login"><svg width="12" height="14" viewBox="0 0 12 14"><rect x="1" y="6" width="10" height="8" fill="#0d5aa6"/><path d="M3 6V4a3 3 0 016 0v2" fill="none" stroke="#0d5aa6" stroke-width="2"/></svg>LOGIN</div>
</header>

<section class="hero">
  <div class="abs" role="img" aria-label="Warehouse aisle with three workers in hard hats and safety vests" style="inset:0"></div>
  <div class="shade"></div>
  <h1 class="hero-title">VELMIRA</h1>
  <p class="hero-sub">We are a marketplace for warehouses</p>
  <a class="hero-btn" style="left:422px">FIND SPACE</a>
  <a class="hero-btn" style="left:609px">LIST SPACE</a>
  <div class="dots"><span class="on"></span><span></span><span></span><span></span></div>
</section>

<aside class="ad" aria-label="Advertising banner">
  <div class="tag">Only this<br>week!</div>
  <div class="product" role="img" aria-label="Laptop with colourful screen"></div>
  <div class="head">Double the SSD storage for free</div>
  <div class="small">when you buy a NOVRA laptop online</div>
  <div class="more">More info ›</div>
</aside>

<section>
  <div class="welcome-box">
    <h2>WELCOME TO VELMIRA</h2>
    <p>Nam libero tempore, cum soluta nobis est eligendi optio cumque nihil impedit quo minus id quod maxime placeat facere possimus, omnis voluptas assumenda est, omnis dolor repellendus. Temporibus autem quibusdam et aut officiis debitis aut rerum necessitatibus saepe eveniet ut et voluptates repudiandae sint et molestiae non recusanda ue earum rerum hic tenetur.</p>
    <a class="btn-outline" style="left:55px;top:316px;width:146px;height:52px;font-size:15px">READ MORE</a>
  </div>
  <div class="video" role="img" aria-label="Video still of two men checking a laptop among cardboard boxes">
    <div class="play"><svg width="60" height="60" viewBox="0 0 60 60"><path d="M24 19l18 11-18 11z" fill="#111"/></svg></div>
  </div>
</section>

<section class="solutions">
  <h2 class="section-title" style="top:70px">SOLUTIONS</h2>

  <div class="sol" style="left:99px">
    <svg width="100" height="90" viewBox="0 0 100 90"><path d="M4 30L50 6l46 24v8H4z" fill="#0d3f8f"/><rect x="10" y="38" width="80" height="48" fill="#0d3f8f"/><g fill="#fff"><rect x="22" y="50" width="14" height="14"/><rect x="43" y="50" width="14" height="14"/><rect x="64" y="50" width="14" height="14"/><rect x="22" y="68" width="14" height="14"/><rect x="43" y="68" width="14" height="14"/><rect x="64" y="68" width="14" height="14"/></g></svg>
    <h3>Inventory Overflow</h3>
    <p>Nam libero tempore, cum soluta nobis est eli ge ndi optio cumque nihil impedit quo id qu od maxime placeat facere pos.</p>
    <a class="read" style="top:276px">READ MORE</a>
  </div>

  <div class="sol" style="left:448px">
    <svg width="100" height="100" viewBox="0 0 100 100"><path d="M50 32l18 9v20l-18 9-18-9V41z" fill="#0d3f8f"/><path d="M32 41l18 9 18-9M50 50v20" stroke="#fff" stroke-width="2" fill="none"/><g stroke="#0d3f8f" stroke-width="3" fill="#0d3f8f"><line x1="50" y1="26" x2="50" y2="8"/><path d="M44 12l6-8 6 8z"/><line x1="50" y1="76" x2="50" y2="94"/><path d="M44 90l6 8 6-8z"/><line x1="26" y1="51" x2="8" y2="51"/><path d="M12 45l-8 6 8 6z"/><line x1="74" y1="51" x2="92" y2="51"/><path d="M88 45l8 6-8 6z"/><line x1="30" y1="30" x2="16" y2="16"/><line x1="70" y1="30" x2="84" y2="16"/><line x1="30" y1="72" x2="16" y2="86"/><line x1="70" y1="72" x2="84" y2="86"/></g></svg>
    <h3>Manage distribution</h3>
    <p>Nam libero tempore, cum soluta nobis est eli ge ndi optio cumque nihil impedit quo id qu od maxime placeat facere pos.</p>
    <a class="read" style="top:276px">READ MORE</a>
  </div>

  <div class="sol" style="left:815px">
    <svg width="100" height="100" viewBox="0 0 100 100"><circle cx="42" cy="44" r="34" fill="none" stroke="#0d3f8f" stroke-width="8"/><path d="M42 22v24h16" fill="none" stroke="#0d3f8f" stroke-width="7"/><g fill="#0d3f8f" stroke="#fff" stroke-width="2"><ellipse cx="72" cy="86" rx="18" ry="7"/><ellipse cx="72" cy="78" rx="18" ry="7"/><ellipse cx="72" cy="70" rx="18" ry="7"/></g></svg>
    <h3>Affordable Cost &amp; Time</h3>
    <p>Nam libero tempore, cum soluta nobis est eli ge ndi optio cumque nihil impedit quo id qu od maxime placeat facere pos.</p>
    <a class="read" style="top:276px">READ MORE</a>
  </div>
</section>

<section class="reviews">
  <h2 class="section-title" style="top:70px">CLIENT REVIEWS</h2>
  <div class="arrow-btn" style="left:28px"><svg width="12" height="14" viewBox="0 0 12 14"><path d="M9 2L3 7l6 5" fill="none" stroke="#fff" stroke-width="2"/></svg></div>
  <div class="arrow-btn" style="left:1131px"><svg width="12" height="14" viewBox="0 0 12 14"><path d="M3 2l6 5-6 5" fill="none" stroke="#fff" stroke-width="2"/></svg></div>

  <div class="review" style="left:96px">
    <div class="avatar" role="img" aria-label="Client portrait"></div>
    <p class="quote"><b>“</b>At vero eos et accusamus et iustodio dignissimos ducimus qui blanditiipraesnt ium voluptatum deleniti atq.</p>
    <p class="who"><strong>MARA ELLISON</strong><em>Financial Services Professional</em></p>
    <div class="stars"><svg width="100" height="18" viewBox="0 0 100 18"><g fill="#f2c200"><path id="s" d="M9 1l2.4 5.2 5.6.6-4.2 3.8 1.2 5.6L9 13.4 4 16.2l1.2-5.6L1 6.8l5.6-.6z"/><use href="#s" x="20"/><use href="#s" x="40"/><use href="#s" x="60"/></g><use href="#s" x="80" fill="none" stroke="#f2c200" stroke-width="1.3"/></svg></div>
  </div>

  <div class="review" style="left:445px">
    <div class="avatar" role="img" aria-label="Client portrait"></div>
    <p class="quote"><b>“</b>At vero eos et accusamus et iustodio dignissimos ducimus qui blanditiipraesnt ium voluptatum deleniti atqu.</p>
    <p class="who"><strong>TOVAN R. PELLIER</strong><em>National Urban Fellow at the Houston</em></p>
    <div class="stars"><svg width="100" height="18" viewBox="0 0 100 18"><defs><linearGradient id="half"><stop offset="50%" stop-color="#f2c200"/><stop offset="50%" stop-color="transparent"/></linearGradient></defs><g fill="#f2c200"><use href="#s"/><use href="#s" x="20"/><use href="#s" x="40"/><use href="#s" x="60"/></g><use href="#s" x="80" fill="url(#half)" stroke="#f2c200" stroke-width="1.3"/></svg></div>
  </div>

  <div class="review" style="left:792px">
    <div class="avatar" role="img" aria-label="Client portrait"></div>
    <p class="quote"><b>“</b>At vero eos et accusamus et iustodio dignissimos ducimus qui blanditiipraesnt ium voluptatum deleniti atq.</p>
    <p class="who"><strong>INA CORVETT</strong><em>Creative Strategist | Entrepreneur &amp; Upcoming</em></p>
    <div class="stars"><svg width="100" height="18" viewBox="0 0 100 18"><g fill="#f2c200"><use href="#s"/><use href="#s" x="20"/><use href="#s" x="40"/><use href="#s" x="60"/></g><use href="#s" x="80" fill="none" stroke="#f2c200" stroke-width="1.3"/></svg></div>
  </div>
</section>

<section>
  <h2 class="section-title blog-title">LATEST BLOG</h2>
  <svg width="0" height="0" style="position:absolute"><defs>
    <symbol id="cal" viewBox="0 0 14 14"><rect x="1" y="2" width="12" height="11" fill="#0d3f8f"/><rect x="2.5" y="5.5" width="9" height="6" fill="#fff"/><rect x="3" y="0" width="2" height="3" fill="#0d3f8f"/><rect x="9" y="0" width="2" height="3" fill="#0d3f8f"/></symbol>
    <symbol id="usr" viewBox="0 0 14 14"><circle cx="7" cy="4" r="3.2" fill="#0d3f8f"/><path d="M1 14a6 6 0 0112 0z" fill="#0d3f8f"/></symbol>
  </defs></svg>

  <article class="post" style="left:99px">
    <div class="img" role="img" aria-label="Aerial view of a distribution centre with parked trucks" style="background:linear-gradient(180deg,#b7c6d3 0%,#9aa7b0 40%,#6f7f4d 70%,#587034 100%)"></div>
    <h3>Finibus Bonorum et Malorum</h3>
    <div class="meta"><svg width="14" height="14"><use href="#cal"/></svg>25/09/2017<span class="sep"></span><svg width="14" height="14"><use href="#usr"/></svg>John</div>
    <p>Nemo enim ipsam voluptatem quia volupta asperna tur aut odit aut fugit, sed quia conseq.</p>
    <a class="read">READ MORE</a>
  </article>

  <article class="post" style="left:437px">
    <div class="img" role="img" aria-label="Two logistics staff reviewing data on a computer screen" style="background:linear-gradient(135deg,#3b3a38,#a88d6a 50%,#d8c3a0)"></div>
    <h3>Finibus Bonorum et Malorum</h3>
    <div class="meta"><svg width="14" height="14"><use href="#cal"/></svg>25/09/2017<span class="sep"></span><svg width="14" height="14"><use href="#usr"/></svg>John</div>
    <p>Nemo enim ipsam voluptatem quia volupta asperna tur aut odit aut fugit, sed quia conseq.</p>
    <a class="read">READ MORE</a>
  </article>

  <article class="post" style="left:778px">
    <div class="img" role="img" aria-label="Tall warehouse shelving stacked with cartons" style="background:linear-gradient(90deg,#6a5237,#c8ab84 50%,#6a5237)"></div>
    <h3>Finibus Bonorum et Malorum</h3>
    <div class="meta"><svg width="14" height="14"><use href="#cal"/></svg>25/09/2017<span class="sep"></span><svg width="14" height="14"><use href="#usr"/></svg>John</div>
    <p>Nemo enim ipsam voluptatem quia volupta asperna tur aut odit aut fugit, sed quia conseq.</p>
    <a class="read">READ MORE</a>
  </article>
</section>

<section>
  <div class="contact-img" role="img" aria-label="Empty warehouse interior with long rows of stocked pallet racks"></div>
  <div class="contact">
    <h2>GET IN TOUCH</h2>
    <div class="field" style="left:52px;top:140px;width:226px">First Name</div>
    <div class="field" style="left:286px;top:140px;width:226px">Last Name</div>
    <div class="field" style="left:52px;top:195px;width:226px">Email Address</div>
    <div class="field" style="left:286px;top:195px;width:226px">Phone Number</div>
    <div class="field" style="left:52px;top:250px;width:460px;height:80px">Message</div>
    <a class="submit">SUBMIT</a>
  </div>
</section>

<footer class="footer">
  <div class="logo" style="left:99px;top:3652px">
    <span class="mark" style="width:54px;height:54px"></span><span class="name" style="font-size:38px">VELMIRA</span>
  </div>

  <h4 style="left:409px">Quick Links</h4>
  <ul class="links"><li>Help</li><li>FAQ</li><li>Support</li><li>Sitemap</li><li>Terms Of Use</li><li>Privacy Statement</li></ul>

  <h4 style="left:601px">Newsletter Subscription</h4>
  <p class="news-text">Register your Email Address to get information about us</p>
  <div class="news-input">Email Address</div>
  <a class="btn-outline subscribe">SUBSCRIBE</a>

  <h4 style="left:919px">Contact Us</h4>
  <div class="contact-item" style="top:3624px"><svg width="12" height="16" viewBox="0 0 12 16"><path d="M6 0a6 6 0 00-6 6c0 4.5 6 10 6 10s6-5.5 6-10a6 6 0 00-6-6z" fill="#0d3f8f"/><circle cx="6" cy="6" r="2.2" fill="#fff"/></svg><span>P.O BOX 58<br>HARLOWE, NY 10420</span></div>
  <div class="contact-item" style="top:3690px"><svg width="14" height="14" viewBox="0 0 14 14"><path d="M3 0l3 3.5-1.8 2a8 8 0 004.3 4.3l2-1.8L14 11l-2 3C6 14 0 8 0 2z" fill="#0d3f8f"/></svg><span>1 555 010 2040</span></div>
  <div class="contact-item" style="top:3738px"><svg width="16" height="12" viewBox="0 0 16 12"><rect width="16" height="12" fill="#0d3f8f"/><path d="M0 0l8 6 8-6" fill="none" stroke="#fff" stroke-width="1.4"/></svg><span>info@velmira.com</span></div>

  <div class="divider"></div>
  <p class="copy">Copyrights © 2018, Velmira. All rights reserved.</p>
  <span class="social" style="left:932px"></span>
  <span class="social" style="left:976px"></span>
  <span class="social" style="left:1019px"></span>
  <span class="social" style="left:1063px"></span>
</footer>

</body>
</html>
```